Electrical company needs professional eye catching business cards

I am an electrician who needs business cards. I have attached two images which you can use. The file ab.jpg I would atleast like to be used. The file named back.jpg can be used on the back or not... up to you.

The information on my business cards I will have displayed will be-
My name
Mobile number
web site url
Licence number
ABN

Also as another request, I would like the word "Electrician" on the front of the card somewhere. Maybe under my name or something?

Industry/Entity Type

Electrician

```html
<!DOCTYPE html>
<html lang="en">
<head>
<meta charset="utf-8">
<title>Kestrel Installations – Business Card</title>
<link rel="stylesheet" href="https://fonts.googleapis.com/css2?family=Open+Sans:wght@400;600&display=swap">
<style>
  :root {
    --bg: #e4e4e6;
    --charcoal: #333335;
    --charcoal-line: #4a4a4d;
    --paper: #fbfbfb;
    --brand-blue: #2c2c9c;
    --brand-blue-deep: #24247f;
    --ink: #3d4450;
    --white: #ffffff;
    --muted: #d9d9dc;
  }
  * { box-sizing: border-box; margin: 0; padding: 0; }
  html, body { width: 1200px; height: 900px; overflow: hidden; }
  body {
    background: var(--bg);
    font-family: "Open Sans", Arial, sans-serif;
    position: relative;
  }
  .card {
    position: absolute;
    left: 280px;
    width: 640px;
    height: 366px;
    border-radius: 6px;
    overflow: hidden;
    box-shadow: 0 6px 18px rgba(0,0,0,0.18);
  }
  .card--front { top: 48px; display: flex; }
  .card--back { top: 476px; }

  /* Front */
  .contact-panel {
    width: 58%;
    background: var(--charcoal);
    position: relative;
    color: var(--muted);
  }
  .identity {
    position: absolute;
    right: 70px;
    top: 48px;
    text-align: right;
  }
  .identity__name {
    font-size: 24px;
    font-weight: 400;
    color: var(--white);
    letter-spacing: 0.5px;
  }
  .identity__role { font-size: 15px; margin-top: -2px; }
  .contact-list {
    position: absolute;
    right: 0;
    top: 132px;
    width: 100%;
    list-style: none;
  }
  .contact-list__item {
    display: flex;
    justify-content: flex-end;
    align-items: center;
    height: 52px;
    border-bottom: 1px solid var(--charcoal-line);
    margin-left: 60px;
  }
  .contact-list__item:last-child { border-bottom: none; }
  .contact-list__text { font-size: 16px; margin-right: 18px; }
  .contact-list__icon {
    width: 52px;
    height: 52px;
    background: var(--brand-blue);
    display: flex;
    align-items: center;
    justify-content: center;
    border-bottom: 1px solid var(--charcoal);
  }
  .brand-panel {
    flex: 1;
    background: var(--paper);
    display: flex;
    flex-direction: column;
    align-items: center;
    justify-content: center;
    color: var(--ink);
  }
  .brand-mark {
    width: 58px; height: 58px;
    background: var(--brand-blue);
    border-radius: 6px;
    margin-bottom: 14px;
  }
  .brand-name { font-size: 27px; font-weight: 600; line-height: 1.1; text-align: center; }
  .brand-abn { font-size: 16px; margin-top: 4px; }

  /* Back */
  .card--back {
    background: linear-gradient(160deg, var(--brand-blue) 0%, var(--brand-blue-deep) 100%);
    display: flex;
    flex-direction: column;
    align-items: center;
    justify-content: center;
    color: var(--white);
  }
  .card--back .brand-mark {
    background: var(--white);
    width: 84px; height: 66px;
    margin-bottom: 10px;
  }
  .card--back .brand-name { font-size: 52px; letter-spacing: -0.5px; }
</style>
</head>
<body>
  <section class="card card--front">
    <div class="contact-panel">
      <div class="identity">
        <p class="identity__name">YOUR NAME</p>
        <p class="identity__role">Electrician</p>
      </div>
      <ul class="contact-list">
        <li class="contact-list__item">
          <span class="contact-list__text">Licence number</span>
          <span class="contact-list__icon">
            <svg width="20" height="20" viewBox="0 0 20 20"><circle cx="10" cy="10" r="7" fill="none" stroke="#fff" stroke-width="2"/></svg>
          </span>
        </li>
        <li class="contact-list__item">
          <span class="contact-list__text">Your Phone Number</span>
          <span class="contact-list__icon">
            <svg width="22" height="20" viewBox="0 0 22 20"><path d="M2 7c0-3 4-4 9-4s9 1 9 4v2h-4V7H6v2H2z" fill="#fff"/><rect x="5" y="10" width="12" height="8" rx="1" fill="none" stroke="#fff" stroke-width="1.6"/><circle cx="11" cy="14" r="2" fill="#fff"/></svg>
          </span>
        </li>
        <li class="contact-list__item">
          <span class="contact-list__text">Web Site URL</span>
          <span class="contact-list__icon">
            <svg width="24" height="22" viewBox="0 0 24 22"><rect x="2" y="2" width="20" height="13" rx="1" fill="none" stroke="#fff" stroke-width="1.8"/><path d="M9 19h6M12 15v4" stroke="#fff" stroke-width="1.8"/></svg>
          </span>
        </li>
      </ul>
    </div>
    <div class="brand-panel">
      <span class="brand-mark"></span>
      <p class="brand-name">Kestrel Installations</p>
      <p class="brand-abn">ABN</p>
    </div>
  </section>

  <section class="card card--back">
    <span class="brand-mark"></span>
    <p class="brand-name">Kestrel Installations</p>
  </section>
</body>
</html>
```